Zielgruppe
Psychologische Beratung für Einzelpersonen
Aufgabenstellung
Der Flyer soll leichter & mit weniger Text werden. Ein anderes Bild, evt. Auch Fronttext wechseln. Das Logo soll der Wassertropfen bleiben. Format: DIN lang (9,8 x 21 cm)

```html
<!DOCTYPE html>
<html lang="de">
<head>
<meta charset="utf-8">
<title>Flyer Psychologische Beratung Felbrunn</title>
<link href="https://fonts.googleapis.com/css2?family=Exo+2:wght@400;500;700;800&display=swap" rel="stylesheet">
<style>
  :root {
    --navy: #1b2f7a;
    --navy-deep: #13296b;
    --blue-mid: #2c5aa0;
    --blue-light: #4a86c8;
    --lavender: #d6dcf2;
    --ink: #2a3590;
    --page: #eceef0;
    --white: #ffffff;
    --photo-grey: #dedede;
  }
  * { box-sizing: border-box; margin: 0; padding: 0; }
  html, body { width: 1200px; height: 949px; overflow: hidden; background: var(--page); }
  body { position: relative; font-family: "Exo 2", Arial, sans-serif; }

  .panel { position: absolute; left: 138px; width: 893px; background: var(--white); overflow: hidden; }
  .panel--back { top: 61px; height: 415px; }
  .panel--front { top: 495px; height: 417px; }
  .panel svg.shapes { position: absolute; inset: 0; }

  .back-title { position: absolute; left: 37px; top: 19px; color: var(--white); font-weight: 800; font-size: 19px; letter-spacing: 0.2px; }
  .needs { position: absolute; left: 37px; top: 64px; width: 390px; list-style: none; color: var(--white); font-size: 12.5px; line-height: 15px; }
  .needs li { position: relative; padding-left: 17px; margin-bottom: 13px; }
  .needs li::before { content: "•"; position: absolute; left: 1px; top: 0; }
  .about { position: absolute; left: 464px; top: 62px; width: 392px; color: var(--white); font-size: 12.5px; line-height: 19px; text-align: justify; hyphens: auto; }

  .portrait { position: absolute; left: 0; top: 283px; width: 134px; height: 111px; border-bottom-right-radius: 22px;
    background: linear-gradient(160deg, #e4e4e4 0%, #d2ccc6 55%, #c9c1b9 100%); }

  .contact { position: absolute; top: 349px; color: var(--ink); font-size: 11px; line-height: 15px; }
  .contact--name { left: 158px; }
  .contact--address { left: 372px; top: 347px; }
  .contact--web { left: 627px; }
  .contact strong { display: block; font-weight: 800; font-size: 12.5px; margin-bottom: 3px; letter-spacing: 0.2px; }
  .contact .url { font-weight: 700; }

  .badge { position: absolute; border-radius: 50%; color: var(--white); font-weight: 800; text-align: center; display: flex; align-items: center; justify-content: center; line-height: 1.05;
    background: radial-gradient(circle at 70% 70%, var(--blue-light), var(--navy) 75%);
    box-shadow: 0 0 0 5px rgba(214,220,242,0.85); }
  .badge--back { left: 744px; top: 223px; width: 106px; height: 106px; font-size: 15px; transform: rotate(-10deg); }
  .badge--front { left: 646px; top: 206px; width: 132px; height: 132px; font-size: 19px; transform: rotate(-10deg); }

  .photo-flower { position: absolute; left: 150px; top: 0; width: 743px; height: 300px;
    background: radial-gradient(ellipse at 58% 45%, #f6dc1c 0 26%, #e8d33a 38%, #b9d35c 58%, #9cc85a 80%);
    -webkit-mask-image: linear-gradient(90deg, transparent 0, #000 28%); mask-image: linear-gradient(90deg, transparent 0, #000 28%); }
  .drop { position: absolute; left: 25px; top: 55px; width: 200px; height: 155px; border-radius: 50%;
    background: radial-gradient(ellipse at 50% 55%, #8fa7e0 0, #c7d3f2 45%, rgba(255,255,255,0) 72%); }
  .brand { position: absolute; left: 42px; top: 28px; display: flex; align-items: center; gap: 8px; color: var(--ink); font-size: 17px; font-weight: 500; }
  .brand-dot { width: 11px; height: 11px; border-radius: 50%; background: var(--blue-light); }

  .claim { position: absolute; left: 65px; top: 314px; color: var(--ink); font-size: 31px; line-height: 38px; font-weight: 400; letter-spacing: -0.3px; }
  .claim b { font-weight: 800; }
</style>
</head>
<body>

<section class="panel panel--back">
  <svg class="shapes" width="893" height="415" viewBox="0 0 893 415" aria-hidden="true">
    <defs>
      <linearGradient id="backBlue" x1="0" y1="0" x2="1" y2="1">
        <stop offset="0" stop-color="#13296b"/>
        <stop offset="0.55" stop-color="#234a92"/>
        <stop offset="1" stop-color="#4a86c8"/>
      </linearGradient>
    </defs>
    <path d="M0,0 H893 V222 C700,262 350,300 0,252 Z" fill="url(#backBlue)"/>
    <path d="M0,262 C350,310 700,272 893,228 L893,238 C700,292 380,336 0,284 Z" fill="var(--navy)"/>
    <path d="M0,284 C380,336 700,292 893,238 L893,242 C700,298 380,342 0,288 Z" fill="var(--lavender)"/>
    <path d="M0,254 C350,302 700,264 893,224" fill="none" stroke="var(--white)" stroke-width="3"/>
  </svg>

  <h1 class="back-title">MÖCHTEN SIE MEHR LUST UND FREUDE AM LEBEN?</h1>
  <ul class="needs">
    <li>Sie stecken in einer persönlichen Krise</li>
    <li>Sie wollen Ihr Selbstvertrauen stärken</li>
    <li>Sie sind beruflich oder privat stark überlastet</li>
    <li>Sie möchten Ängste und Blockaden überwinden</li>
    <li>Sie suchen Unterstützung bei Entscheidungen</li>
  </ul>
  <div class="about">
    <p>Psychologische Beratung hilft, in schwierigen Situationen Klarheit zu gewinnen, Altes loszulassen und sich neu zu orientieren. Wir gehen von Ihren Erfahrungen und Bedürfnissen aus, stärken Ihre Ressourcen und eröffnen neue Handlungsmöglichkeiten.</p>
  </div>

  <div class="badge badge--back">ICH FREUE<br>MICH AUF<br>SIE!</div>

  <div class="portrait" role="img" aria-label="Porträtfoto der Beraterin"></div>

  <div class="contact contact--name"><strong>MIRJAM BODTKE</strong>Eidg. dipl. Psychosoziale Beraterin,<br>Lösungsorientierter Coach</div>
  <div class="contact contact--address">Lindengasse 14, 8712 Felbrunn<br>Telefon +41 78 000 14 36<br>Email mirjam.bodtke@beratung-felbrunn.ch</div>
  <div class="contact contact--web"><strong>WEITERE INFORMATIONEN</strong>finden Sie auf meiner Homepage<br><span class="url">www.beratung-felbrunn.ch</span></div>
</section>

<section class="panel panel--front">
  <div class="photo-flower" role="img" aria-label="Foto einer gelben Löwenzahnblüte vor grünem Hintergrund"></div>
  <svg class="shapes" width="893" height="417" viewBox="0 0 893 417" aria-hidden="true">
    <path d="M0,236 C300,300 620,300 893,262 V417 H0 Z" fill="var(--white)"/>
    <path d="M0,222 C300,286 620,290 893,248 L893,262 C620,304 300,300 0,236 Z" fill="var(--navy)"/>
    <path d="M0,236 C300,300 620,304 893,262 L893,266 C620,310 300,306 0,240 Z" fill="var(--lavender)"/>
  </svg>

  <div class="drop" role="img" aria-label="Illustration eines Wassertropfens mit Spritzkrone"></div>
  <div class="brand"><span>Bodtke Beratung</span><span class="brand-dot"></span></div>

  <div class="badge badge--front">KRANKEN-<br>KASSEN<br>ANERKANNT</div>

  <p class="claim"><b>KLARHEIT</b> GEWINNEN,<br>NEU <b>AUFBLÜHEN</b>!</p>
</section>

</body>
</html>
```